MindHarbr Powerpoint Presentation Template

I am looking for a PowerPoint template that I can use for my presentations. I have attached a copy of my logo that your community has previously designed for me. My presentations are typically visual with very little text being used.
I have included my current presentation style using my old corporate colours (they are very different). There is one condition, the template must not have a white background as this detracts the focus of the crowd away from the presenter (which defeats the purpose of having a presenter in the first place).
Thank you for your time in coming up with a design!
Lorn
Look and feel
Each slider illustrates characteristics of the customer's brand and the style your logo design should communicate.

```html
<!DOCTYPE html>
<html lang="en">
<head>
<meta charset="utf-8">
<title>MindHarbr Presentation Template</title>
<link href="https://fonts.googleapis.com/css2?family=Montserrat:wght@400;600;700&display=swap" rel="stylesheet">
<style>
:root{
  --blue:#1ea4ea;
  --blue-deep:#0d6fae;
  --navy:#0a141d;
  --dark:#141c24;
  --panel:#1d2731;
  --white:#ffffff;
  --mute:#9fb3c2;
  --stage:#b7b9bb;
}
*{margin:0;padding:0;box-sizing:border-box}
html,body{width:1200px;height:2260px;overflow:hidden;background:var(--stage);font-family:"Montserrat",sans-serif}
.deck{display:grid;grid-template-columns:560px 560px;column-gap:24px;row-gap:125px;padding:93px 28px;width:1200px;height:2260px}
.slide{position:relative;width:560px;height:315px;overflow:hidden;background:var(--dark);color:var(--white)}
.photo{position:absolute;background:linear-gradient(135deg,#3f5566,#22313d 60%,#16222c)}
.photo.blue{background:linear-gradient(135deg,#4fb8ee,#1c7fbf 55%,#0e4c78)}
.photo.light{background:linear-gradient(135deg,#dfe6ec,#9aa9b6 60%,#5d6f7e)}
.photo.warm{background:linear-gradient(135deg,#d9c4a6,#a38463 60%,#5e4a38)}
.logo{position:absolute;display:flex;align-items:center;gap:6px;font-weight:700;color:var(--white)}
.logo i{display:block;border-radius:50%;border:2px solid var(--blue)}
.logo.sm{font-size:11px}.logo.sm i{width:12px;height:12px}
.logo.md{font-size:16px}.logo.md i{width:18px;height:18px}
.logo.lg{font-size:22px}.logo.lg i{width:24px;height:24px}
.title{position:absolute;font-weight:700;color:var(--blue);line-height:1.05}
.small{position:absolute;font-size:8px;line-height:1.5;color:var(--mute)}
.footer{position:absolute;left:0;right:0;bottom:0;height:14px;background:var(--navy);display:flex;align-items:center;justify-content:space-between;padding:0 10px;font-size:6px;color:var(--mute);letter-spacing:.5px}
.footer b{display:block;width:14px;height:14px;background:var(--blue);color:var(--white);font-size:6px;text-align:center;line-height:14px}
.avatar{position:absolute;width:46px;height:46px;border-radius:50%;border:2px solid var(--white);background:linear-gradient(135deg,#6f8496,#2f4150)}
.tab{position:absolute;height:16px;background:var(--navy);color:var(--white);font-size:7px;font-weight:600;text-align:center;line-height:16px}
.icon{position:absolute;width:42px;height:42px;border-radius:50%;border:2px solid var(--blue);display:flex;align-items:center;justify-content:center}
.head{position:absolute;font-size:9px;font-weight:600;text-align:center;width:80px}
table{position:absolute;border-collapse:collapse;font-size:7px;color:var(--white)}
td,th{border-bottom:1px solid rgba(255,255,255,.35);padding:3px 8px;text-align:left}
th{background:var(--navy);font-weight:600}
</style>
</head>
<body>
<main class="deck">

  <!-- Title slide -->
  <section class="slide title-slide">
    <div class="photo blue" style="left:240px;top:0;width:320px;height:301px;clip-path:polygon(28% 0,100% 0,100% 100%,0 100%)" role="img" aria-label="Business people working at a laptop, blue tinted"></div>
    <svg style="position:absolute;left:0;top:0" width="560" height="315"><polygon points="0,60 300,60 220,175 0,175" fill="#1ea4ea" opacity=".9"/></svg>
    <div class="title" style="left:22px;top:20px;font-size:26px;color:var(--white)">Psychological<br>Safety</div>
    <div class="small" style="left:22px;top:80px;width:180px;color:var(--white)">Building trust so every voice can be heard</div>
    <div class="logo md" style="left:22px;top:200px"><i></i>MindHarbr</div>
    <div class="footer"><span>Psychological Safety Workshop</span><b>1</b></div>
  </section>

  <!-- Title slide variant -->
  <section class="slide title-slide-alt">
    <div class="photo light" style="left:210px;top:0;width:350px;height:301px" role="img" aria-label="Team meeting around a table in a bright office"></div>
    <svg style="position:absolute;left:0;top:0" width="560" height="315"><polygon points="0,0 240,0 170,170 0,170" fill="#141c24"/><polygon points="0,170 170,170 240,301 0,301" fill="#ffffff"/><polygon points="170,170 240,0 250,0 180,170" fill="#1ea4ea"/></svg>
    <div class="title" style="left:22px;top:20px;font-size:26px">Psychological<br>Safety</div>
    <div class="small" style="left:22px;top:80px;width:160px;color:var(--white)">Building trust so every voice can be heard</div>
    <div class="logo md" style="left:22px;top:225px;color:var(--navy)"><i></i>MindHarbr</div>
    <div class="footer"><span>Psychological Safety Workshop</span><b>2</b></div>
  </section>

  <!-- About us -->
  <section class="slide about">
    <div class="title" style="left:22px;top:18px;font-size:18px">About Us</div>
    <div class="logo sm" style="right:18px;top:18px"><i></i>MindHarbr</div>
    <div class="photo light" style="left:22px;top:55px;width:200px;height:120px" role="img" aria-label="Colleagues in a meeting room"></div>
    <div class="small" style="left:245px;top:70px;width:220px;color:var(--white)">• Safe teams speak up early<br>• Leaders model open listening<br>• Mistakes become shared learning</div>
    <div class="photo" style="left:22px;top:195px;width:150px;height:85px" role="img" aria-label="Team discussion"></div>
    <div class="photo blue" style="left:182px;top:195px;width:150px;height:85px" role="img" aria-label="Office workspace"></div>
    <div class="photo light" style="left:342px;top:195px;width:150px;height:85px" role="img" aria-label="Presenter with audience"></div>
    <div class="footer"><span>Psychological Safety Workshop</span><b>3</b></div>
  </section>

  <!-- Team -->
  <section class="slide team">
    <div style="position:absolute;left:0;top:0;width:560px;height:190px;background:var(--blue)"></div>
    <div class="title" style="left:22px;top:18px;font-size:18px;color:var(--white)">Meet Our Team</div>
    <div class="logo sm" style="right:18px;top:18px"><i></i>MindHarbr</div>
    <div class="avatar" style="left:97px;top:62px" role="img" aria-label="Team member portrait"></div>
    <div class="avatar" style="left:257px;top:62px" role="img" aria-label="Team member portrait"></div>
    <div class="avatar" style="left:417px;top:62px" role="img" aria-label="Team member portrait"></div>
    <div class="small" style="left:60px;top:118px;width:120px;text-align:center;color:var(--white)"><b>Person Name</b><br>Team Role<br>Short bio text here</div>
    <div class="small" style="left:220px;top:118px;width:120px;text-align:center;color:var(--white)"><b>Person Name</b><br>Team Role<br>Short bio text here</div>
    <div class="small" style="left:380px;top:118px;width:120px;text-align:center;color:var(--white)"><b>Person Name</b><br>Team Role<br>Short bio text here</div>
    <div class="photo" style="left:0;top:190px;width:560px;height:111px;opacity:.6" role="img" aria-label="Dark office background"></div>
    <div class="footer"><span>Psychological Safety Workshop</span><b>4</b></div>
  </section>

  <!-- Section divider -->
  <section class="slide section">
    <div class="photo" style="left:0;top:0;width:560px;height:315px;background:linear-gradient(135deg,#2b3845,#101820)" role="img" aria-label="Dimmed photo of a business meeting"></div>
    <div class="logo md" style="left:50%;top:95px;transform:translateX(-50%)"><i></i>MindHarbr</div>
    <div class="small" style="left:0;width:560px;top:145px;text-align:center;font-size:11px;color:var(--white)">This is what we call</div>
    <div class="title" style="left:0;width:560px;top:165px;text-align:center;font-size:26px">Psychological Safety</div>
  </section>

  <!-- Three column slide -->
  <section class="slide columns" style="background:var(--blue)">
    <div class="title" style="left:22px;top:18px;font-size:18px;color:var(--white)">Slide Title Goes Here</div>
    <div class="logo sm" style="right:18px;top:18px"><i></i>MindHarbr</div>
    <div class="tab" style="left:40px;top:65px;width:150px">Title Goes Here</div>
    <div class="tab" style="left:205px;top:65px;width:150px">Title Goes Here</div>
    <div class="tab" style="left:370px;top:65px;width:150px">Title Goes Here</div>
    <div class="photo light" style="left:40px;top:88px;width:150px;height:95px" role="img" aria-label="Workshop participants"></div>
    <div class="photo" style="left:205px;top:88px;width:150px;height:95px" role="img" aria-label="Team collaboration"></div>
    <div class="photo light" style="left:370px;top:88px;width:150px;height:95px" role="img" aria-label="Office conversation"></div>
    <div class="small" style="left:40px;top:192px;width:150px;color:var(--white)">Add a short caption</div>
    <div class="small" style="left:205px;top:192px;width:150px;color:var(--white)">Add a short caption</div>
    <div class="small" style="left:370px;top:192px;width:150px;color:var(--white)">Add a short caption</div>
    <div class="footer"><span>Psychological Safety Workshop</span><b>6</b></div>
  </section>

  <!-- Icon headings -->
  <section class="slide icons">
    <div style="position:absolute;left:0;top:200px;width:560px;height:101px;background:var(--blue)"></div>
    <div class="logo md" style="left:50%;top:25px;transform:translateX(-50%)"><i></i>MindHarbr</div>
    <div class="icon" style="left:79px;top:95px"><svg width="18" height="18" viewBox="0 0 18 18"><path d="M3 9l4 4 8-9" stroke="#1ea4ea" stroke-width="2" fill="none"/></svg></div>
    <div class="icon" style="left:199px;top:95px"><svg width="18" height="18" viewBox="0 0 18 18"><circle cx="9" cy="9" r="6" stroke="#1ea4ea" stroke-width="2" fill="none"/></svg></div>
    <div class="icon" style="left:319px;top:95px"><svg width="18" height="18" viewBox="0 0 18 18"><path d="M2 9h12M10 5l4 4-4 4" stroke="#1ea4ea" stroke-width="2" fill="none"/></svg></div>
    <div class="icon" style="left:439px;top:95px"><svg width="18" height="18" viewBox="0 0 18 18"><rect x="3" y="3" width="12" height="12" stroke="#1ea4ea" stroke-width="2" fill="none"/></svg></div>
    <div class="head" style="left:60px;top:145px">Heading</div>
    <div class="head" style="left:180px;top:145px">Heading</div>
    <div class="head" style="left:300px;top:145px">Heading</div>
    <div class="head" style="left:420px;top:145px">Heading</div>
    <div class="small" style="left:60px;top:160px;width:80px;text-align:center">Add a short line</div>
    <div class="small" style="left:180px;top:160px;width:80px;text-align:center">Add a short line</div>
    <div class="small" style="left:300px;top:160px;width:80px;text-align:center">Add a short line</div>
    <div class="small" style="left:420px;top:160px;width:80px;text-align:center">Add a short line</div>
    <div class="footer"><span>Psychological Safety Workshop</span><b>7</b></div>
  </section>

  <!-- Split slide -->
  <section class="slide split" style="background:var(--blue)">
    <div style="position:absolute;left:0;top:0;width:220px;height:301px;background:var(--dark)"></div>
    <div class="logo sm" style="left:22px;top:18px"><i></i>MindHarbr</div>
    <div class="title" style="left:22px;top:90px;font-size:22px">Slide Title<br>Goes Here</div>
    <div class="small" style="left:22px;top:150px;width:170px;color:var(--white)">Add your key message here in a few words</div>
    <div class="photo warm" style="left:240px;top:20px;width:140px;height:125px" role="img" aria-label="Hands on a desk with papers"></div>
    <div class="photo light" style="left:395px;top:20px;width:145px;height:125px" role="img" aria-label="Person writing notes"></div>
    <div class="photo warm" style="left:240px;top:160px;width:300px;height:120px" role="img" aria-label="Team planning session"></div>
    <div class="footer"><span>Psychological Safety Workshop</span><b>8</b></div>
  </section>

  <!-- Chart -->
  <section class="slide chart" style="background:var(--blue)">
    <div class="title" style="left:22px;top:18px;font-size:18px;color:var(--white)">Chart Slide</div>
    <div class="logo sm" style="right:18px;top:18px"><i></i>MindHarbr</div>
    <svg style="position:absolute;left:22px;top:70px" width="260" height="200" viewBox="0 0 260 200">
      <rect width="260" height="200" fill="#0a141d" opacity=".85"/>
      <g stroke="#ffffff" stroke-opacity=".2"><line x1="20" y1="40" x2="250" y2="40"/><line x1="20" y1="80" x2="250" y2="80"/><line x1="20" y1="120" x2="250" y2="120"/><line x1="20" y1="160" x2="250" y2="160"/></g>
      <g fill="#1ea4ea">
        <rect x="35" y="110" width="16" height="65"/><rect x="75" y="80" width="16" height="95"/><rect x="115" y="95" width="16" height="80"/><rect x="155" y="60" width="16" height="115"/><rect x="195" y="40" width="16" height="135"/>
      </g>
      <g fill="#ffffff" opacity=".5">
        <rect x="53" y="130" width="10" height="45"/><rect x="93" y="110" width="10" height="65"/><rect x="133" y="120" width="10" height="55"/><rect x="173" y="90" width="10" height="85"/><rect x="213" y="75" width="10" height="100"/>
      </g>
      <line x1="20" y1="175" x2="250" y2="175" stroke="#fff"/>
    </svg>
    <table style="left:310px;top:80px;width:220px">
      <tr><th>Quarter</th><th>Score</th></tr>
      <tr><td>Q1</td><td>42</td></tr>
      <tr><td>Q2</td><td>58</td></tr>
      <tr><td>Q3</td><td>51</td></tr>
      <tr><td>Q4</td><td>69</td></tr>
      <tr><td>Q5</td><td>77</td></tr>
    </table>
    <div class="footer"><span>Psychological Safety Workshop</span><b>9</b></div>
  </section>

  <!-- Contact -->
  <section class="slide contact">
    <div class="photo" style="left:0;top:0;width:560px;height:315px;background:linear-gradient(135deg,#33414d,#0f171e)" role="img" aria-label="Dimmed photo of a handshake"></div>
    <div style="position:absolute;left:0;top:290px;width:560px;height:25px;background:var(--blue)"></div>
    <div class="logo lg" style="left:30px;top:60px"><i></i>MindHarbr</div>
    <div class="title" style="left:30px;top:140px;font-size:14px;color:var(--white)">Contact Us</div>
    <div class="small" style="left:30px;top:162px;color:var(--white);font-size:8px">+1 555 0100<br>hello@mindharbr.com<br>www.mindharbr.com<br>12 Harbour Lane</div>
  </section>

</main>
</body>
</html>
```